Webshop Template

For our Webstore in UK we need a complete Template,
shoppingcart is Magento, the Shop is focussed on Download software,

the name: Appvaultdepot.co.uk

Check out some other good stores, like lumawerk.de

for example the Page from 

www.brenvik.co.uk or

www.lumawerk.de

www.tastenhugo.de

www.klickrabatt.de

The Logodesign which are in Consideration

http://www.artmosaiq.com/design/5520817/logo-design-by-tomasz7kv

http://www.artmosaiq.com/design/5518360/logo-design-by-luisgaviota

http://www.artmosaiq.com/design/5517245/logo-design-by-kestrel-works

http://www.artmosaiq.com/design/5516093/logo-design-by-zumbiloft

http://www.artmosaiq.com/design/5515471/logo-design-by-tivaro

http://www.artmosaiq.com/design/5514902/logo-design-by-blue-fern-graphics-

Target Market(s)

B2C - Consumer Marcet

Industry/Entity Type

Shop

```html
<!DOCTYPE html>
<html lang="en">
<head>
<meta charset="utf-8">
<title>Appvaultdepot.co.uk — Webshop Template</title>
<link rel="stylesheet" href="https://fonts.googleapis.com/css2?family=Arimo:wght@400;700&family=Tinos:wght@700&display=swap">
<style>
:root{
  --bg-dark:#2b2b2b;
  --bg-mid:#3a3a3a;
  --nav:#14202b;
  --gold:#d4ae06;
  --gold-text:#e0b818;
  --white:#ffffff;
  --panel:#ffffff;
  --card-grey:#7b7b7b;
  --btn-dark:#111b24;
  --text-dark:#1a1a1a;
  --line:#cfcfcf;
}
*{box-sizing:border-box;margin:0;padding:0}
html,body{width:1119px;height:1200px;overflow:hidden}
body{
  position:relative;
  font-family:"Arimo",Arial,sans-serif;
  background:linear-gradient(90deg,#2a2a2a 0%,#3b3b3b 25%,#303030 50%,#3c3c3c 75%,#2a2a2a 100%);
  color:var(--text-dark);
}
.abs{position:absolute}

/* top navigation */
.main-nav{left:280px;top:65px;width:501px;height:37px;background:var(--nav)}
.main-nav a{position:absolute;top:11px;color:var(--white);font-size:13px;text-decoration:none}
.user-links{left:814px;top:73px;font-size:13.5px;color:var(--gold-text)}
.user-links .sep{margin:0 10px}

/* main panel */
.main-panel{left:280px;top:102px;width:746px;height:961px;background:var(--panel)}
.logo{left:303px;top:133px;font-size:36px;font-weight:700;color:#000;letter-spacing:.5px}
.cart-summary{left:736px;top:119px;font-size:13.5px;color:#111;display:flex;align-items:center;gap:4px}
.cart-summary .divider{margin:0 10px}
.search-field{left:735px;top:151px;width:227px;height:26px;border:2px solid #e4e4e4;border-radius:3px;font-size:10px;color:#999;padding:6px 8px}
.search-btn{left:969px;top:152px;width:44px;height:24px;background:var(--gold);border-radius:3px;display:flex;align-items:center;justify-content:center}

.featured-bar{left:290px;top:201px;width:655px;height:34px;background:var(--gold);color:var(--white);font-size:16px;padding:9px 16px}
.view-toggle{top:201px;width:22px;height:22px;border:1px solid #ddd}

/* product grid */
.product{width:177px;height:261px}
.product .photo-area{position:absolute;left:0;top:0;width:177px;height:176px;display:flex;align-items:center;justify-content:center}
.product .photo{width:84px;height:100px}
.product .info{position:absolute;left:0;top:176px;width:177px;height:85px;background:var(--card-grey);padding:10px 5px 0}
.product .name{font-size:11px;color:var(--white);white-space:nowrap;overflow:hidden}
.product .price{font-family:"Tinos",Georgia,serif;font-weight:700;font-size:16px;color:var(--white);margin-top:10px}
.product .add-btn{margin-top:3px;width:112px;height:17px;background:var(--btn-dark);color:var(--white);font-size:10px;font-weight:700;text-align:center;line-height:17px;border-radius:2px}
.col-rule{width:1px;background:#9a9a9a}

/* sidebar */
.side-head{left:93px;width:187px;background:var(--white);font-size:16px;color:#111;display:flex;align-items:center;gap:7px;padding-left:11px}
.side-body{left:93px;width:187px;background:var(--gold)}
.cat-list{list-style:none;padding:5px 10px 0 10px}
.cat-list li{height:30.2px;border-bottom:1px dashed rgba(255,255,255,.55);color:var(--white);font-size:14.5px;line-height:30px;padding-left:2px}
.cat-list li:last-child{border-bottom:none}
.thumb{top:668px;height:78px;border:3px solid #8c8c8c}
.email-field{left:104px;top:816px;width:124px;height:27px;background:var(--white);border-radius:14px 0 0 14px;font-size:9.5px;color:#888;padding:8px 10px}
.go-btn{left:226px;top:815px;width:41px;height:29px;background:var(--btn-dark);border-radius:6px;color:var(--white);font-size:16px;text-align:center;line-height:29px}
.cart-text{left:104px;top:913px;font-size:11px;color:#222;line-height:14px}
.cart-btn{top:973px;height:17px;font-size:11px;line-height:17px;padding-left:8px;border-radius:3px}
.cart-btn.view{left:105px;width:77px;background:var(--white);color:#111}
.cart-btn.checkout{left:185px;width:77px;background:var(--btn-dark);color:var(--white)}

/* footer */
.footer-links{left:281px;top:1093px;font-size:13px;color:var(--white)}
.footer-links .sep{margin:0 10px}
.pay-row{left:279px;top:1121px;width:275px;height:32px;background:var(--white);display:flex;gap:4px;padding:3px}
.pay-badge{width:42px;height:26px;border-radius:2px}
</style>
</head>
<body>

<nav class="main-nav abs">
  <a style="left:16px">home</a>
  <a style="left:72px">Latest Softwares</a>
  <a style="left:189px">Freeware</a>
  <a style="left:263px">Top 10</a>
  <a style="left:332px">Delivery Info</a>
  <a style="left:426px">Contact</a>
</nav>
<div class="user-links abs">Welcome Guest<span class="sep">::</span>Login/Register</div>

<div class="main-panel abs"></div>
<div class="logo abs">LOGO</div>

<div class="cart-summary abs">
  <svg width="17" height="14" viewBox="0 0 17 14"><path d="M1 5h15l-2 8H3z" fill="#222"/><path d="M4 5l4-4M13 5L9 1" stroke="#222" stroke-width="1.5" fill="none"/></svg>
  <b>Cart:</b> (2 items :: $567)
  <span class="divider">|</span>
  <svg width="16" height="16" viewBox="0 0 16 16"><circle cx="8" cy="4.5" r="3.5" fill="#222"/><path d="M1 16c0-5 3-7 7-7s7 2 7 7z" fill="#222"/></svg>
  Your Account
</div>
<div class="search-field abs">Search Products</div>
<div class="search-btn abs">
  <svg width="18" height="18" viewBox="0 0 18 18"><circle cx="7.5" cy="7.5" r="5" stroke="#fff" stroke-width="2.5" fill="none"/><path d="M11 11l5 5" stroke="#fff" stroke-width="3"/></svg>
</div>

<div class="featured-bar abs">Featured Products</div>
<div class="view-toggle abs" style="left:960px;border:none">
  <svg width="22" height="22" viewBox="0 0 22 22"><rect x="3" y="3" width="7" height="7" fill="#111"/><rect x="12" y="3" width="7" height="7" fill="#111"/><rect x="3" y="12" width="7" height="7" fill="#111"/><rect x="12" y="12" width="7" height="7" fill="#111"/></svg>
</div>
<div class="view-toggle abs" style="left:991px">
  <svg width="20" height="20" viewBox="0 0 20 20"><g fill="#bbb"><rect x="3" y="4" width="4" height="3"/><rect x="9" y="4" width="8" height="3"/><rect x="3" y="9" width="4" height="3"/><rect x="9" y="9" width="8" height="3"/><rect x="3" y="14" width="4" height="3"/><rect x="9" y="14" width="8" height="3"/></g></svg>
</div>

<!-- column rules -->
<div class="col-rule abs" style="left:470px;top:242px;height:176px"></div>
<div class="col-rule abs" style="left:652px;top:242px;height:176px"></div>
<div class="col-rule abs" style="left:835px;top:242px;height:176px"></div>
<div class="col-rule abs" style="left:470px;top:512px;height:176px"></div>
<div class="col-rule abs" style="left:652px;top:512px;height:176px"></div>
<div class="col-rule abs" style="left:835px;top:512px;height:176px"></div>
<div class="col-rule abs" style="left:470px;top:782px;height:176px"></div>
<div class="col-rule abs" style="left:652px;top:782px;height:176px"></div>
<div class="col-rule abs" style="left:835px;top:782px;height:176px"></div>

<!-- row 1 -->
<div class="product abs" style="left:291px;top:242px">
  <div class="photo-area"><div class="photo" role="img" aria-label="Tax software box, green" style="background:linear-gradient(135deg,#2f6a22,#8fc24a)"></div></div>
  <div class="info"><div class="name">Merino solid vest</div><div class="price">388,11 €</div><div class="add-btn">Add to cart</div></div>
</div>
<div class="product abs" style="left:474px;top:242px">
  <div class="photo-area"><div class="photo" role="img" aria-label="Operating system box with disc, green" style="background:linear-gradient(135deg,#1e8a2c,#dfe9dc)"></div></div>
  <div class="info"><div class="name">COTTON-CASHMERE...</div><div class="price">388,11 €</div><div class="add-btn">Add to cart</div></div>
</div>
<div class="product abs" style="left:656px;top:242px">
  <div class="photo-area"><div class="photo" role="img" aria-label="Office software box, orange" style="background:linear-gradient(135deg,#f6c02a,#e0561c)"></div></div>
  <div class="info"><div class="name">WOOL-CASHMERE CABLE...</div><div class="price">388,11 €</div><div class="add-btn">Add to cart</div></div>
</div>
<div class="product abs" style="left:839px;top:242px">
  <div class="photo-area"><div class="photo" role="img" aria-label="Operating system box, dark blue" style="background:linear-gradient(135deg,#1a1f3a,#3a5fb0)"></div></div>
  <div class="info"><div class="name">Merino polo</div><div class="price">388,11 €</div><div class="add-btn">Add to cart</div></div>
</div>

<!-- row 2 -->
<div class="product abs" style="left:291px;top:512px">
  <div class="photo-area"><div class="photo" role="img" aria-label="Security suite box, teal and red" style="background:linear-gradient(135deg,#2a9a8a,#eef2f2 60%,#d8161b)"></div></div>
  <div class="info"><div class="name">Alpaca shawl-collar...</div><div class="price">388,11 €</div><div class="add-btn">Add to cart</div></div>
</div>
<div class="product abs" style="left:474px;top:512px">
  <div class="photo-area"><div class="photo" role="img" aria-label="Tax software box, red" style="background:linear-gradient(135deg,#c8141a,#e7a53a)"></div></div>
  <div class="info"><div class="name">Marled cotton pullover</div><div class="price">388,11 €</div><div class="add-btn">Add to cart</div></div>
</div>
<div class="product abs" style="left:656px;top:512px">
  <div class="photo-area"><div class="photo" role="img" aria-label="Painting software box, white and blue" style="background:linear-gradient(135deg,#f2f2f2,#9fb0c8)"></div></div>
  <div class="info"><div class="name">Marled cotton cardigan</div><div class="price">388,11 €</div><div class="add-btn">Add to cart</div></div>
</div>
<div class="product abs" style="left:839px;top:512px">
  <div class="photo-area"><div class="photo" role="img" aria-label="Operating system box, blue" style="background:linear-gradient(135deg,#0f4fa8,#5aa0e0)"></div></div>
  <div class="info"><div class="name">MASON SHAWL-COLLAR...</div><div class="price">388,11 €</div><div class="add-btn">Add to cart</div></div>
</div>

<!-- row 3 -->
<div class="product abs" style="left:291px;top:782px">
  <div class="photo-area"><div class="photo" role="img" aria-label="DVD authoring software box, blue and white" style="background:linear-gradient(135deg,#1d56a8,#e8eef6)"></div></div>
  <div class="info"><div class="name">Cotton-cashmere V-neck...</div><div class="price">388,11 €</div><div class="add-btn">Add to cart</div></div>
</div>
<div class="product abs" style="left:474px;top:782px">
  <div class="photo-area"><div class="photo" role="img" aria-label="DVD player software box, red" style="background:linear-gradient(135deg,#d51a1a,#7a0c0c)"></div></div>
  <div class="info"><div class="name">MERINO ASHLAND-STRIPE...</div><div class="price">388,11 €</div><div class="add-btn">Add to cart</div></div>
</div>
<div class="product abs" style="left:656px;top:782px">
  <div class="photo-area"><div class="photo" role="img" aria-label="Red computer mouse" style="width:90px;height:50px;border-radius:14px;background:linear-gradient(135deg,#e2231a,#8a0c08)"></div></div>
  <div class="info"><div class="name">COTTON-CASHMERE ARGYLE...</div><div class="price">388,11 €</div><div class="add-btn">Add to cart</div></div>
</div>
<div class="product abs" style="left:839px;top:782px">
  <div class="photo-area"><div class="photo" role="img" aria-label="Tax software box, green" style="background:linear-gradient(135deg,#2f6a22,#8fc24a)"></div></div>
  <div class="info"><div class="name">Cotton-cashmere cardigan</div><div class="price">388,11 €</div><div class="add-btn">Add to cart</div></div>
</div>

<!-- sidebar: categories -->
<div class="side-head abs" style="top:201px;height:38px">
  <svg width="20" height="17" viewBox="0 0 20 17"><path d="M0 1h4l3 10h10l2-7H6" stroke="#111" stroke-width="2" fill="none"/><rect x="6" y="4" width="12" height="6" fill="#111"/><circle cx="8" cy="15" r="1.7" fill="#111"/><circle cx="16" cy="15" r="1.7" fill="#111"/></svg>
  Shop Our Store
</div>
<div class="side-body abs" style="top:239px;height:374px">
  <ul class="cat-list">
    <li>→&nbsp; Utility Softwares</li>
    <li>→&nbsp; Games</li>
    <li>→&nbsp; Screen Savers</li>
    <li>→&nbsp; Operating Systems</li>
    <li>→&nbsp; Free Softwares</li>
    <li>→&nbsp; Antivirus</li>
    <li>→&nbsp; Browsers</li>
    <li>→&nbsp; Drivers</li>
    <li>→&nbsp; Security Softwares</li>
    <li>→&nbsp; Audio</li>
    <li>→&nbsp; Designing Softwares</li>
    <li>→&nbsp; Video Softwares</li>
  </ul>
</div>

<!-- sidebar: recently viewed -->
<div class="side-head abs" style="top:622px;height:35px">
  <svg width="24" height="16" viewBox="0 0 24 16"><path d="M1 8C5 1 19 1 23 8 19 15 5 15 1 8z" fill="#111"/><circle cx="12" cy="8" r="4.5" fill="#fff"/><circle cx="12" cy="8" r="2.5" fill="#111"/></svg>
  Recently Viewed
</div>
<div class="side-body abs" style="top:657px;height:98px"></div>
<div class="thumb abs" role="img" aria-label="Tax software box, green" style="left:109px;width:72px;background:linear-gradient(135deg,#2f6a22,#8fc24a)"></div>
<div class="thumb abs" role="img" aria-label="Operating system box, blue" style="left:196px;width:70px;background:linear-gradient(135deg,#0f4fa8,#5aa0e0)"></div>

<!-- sidebar: subscribe -->
<div class="side-head abs" style="top:763px;height:38px">
  <svg width="22" height="16" viewBox="0 0 22 16"><rect x="1" y="1" width="20" height="14" fill="#111"/><path d="M1 1l10 8 10-8" stroke="#fff" stroke-width="1.5" fill="none"/></svg>
  Subcribe Now
</div>
<div class="side-body abs" style="top:801px;height:63px"></div>
<div class="email-field abs">enter your email</div>
<div class="go-btn abs">GO</div>

<!-- sidebar: cart -->
<div class="side-head abs" style="top:870px;height:36px">
  <svg width="19" height="16" viewBox="0 0 19 16"><path d="M1 6h17l-2 9H3z" fill="#111"/><path d="M5 6l4-5M14 6L10 1" stroke="#111" stroke-width="1.6" fill="none"/></svg>
  Your Cart
</div>
<div class="side-body abs" style="top:906px;height:99px"></div>
<div class="cart-text abs">No Product Selected<br><br>Shipping: $0.0<br>Total: $0.0</div>
<div class="cart-btn view abs">view cart ▶</div>
<div class="cart-btn checkout abs">check out ▶</div>

<!-- footer -->
<div class="footer-links abs">specials<span class="sep">|</span>our stores<span class="sep">|</span>new products<span class="sep">|</span>top sellers<span class="sep">|</span>terms and conditions</div>
<div class="pay-row abs">
  <div class="pay-badge" style="background:#1a3d8f"></div>
  <div class="pay-badge" style="background:#f08a1c"></div>
  <div class="pay-badge" style="background:#3d86c6"></div>
  <div class="pay-badge" style="background:#2a8a3c;width:24px"></div>
  <div class="pay-badge" style="background:#cc1b1b"></div>
  <div class="pay-badge" style="background:#bfcde0"></div>
</div>

</body>
</html>
```